Copper Ridge Jerky packaging

We are looking for a modern, upmarket packaging for our range of beef jerky. Our existing logo is attached for your reference.
We aim to have our product placed in gastro pubs, craft beer events, bottle shops and hotels. The retail package itself will be 60g net and approximately 17cm x 14cm. There will be 4 flavours (original, chilli, smoked pepper and mongolian).
We would like to see some illustration in the design to showcase the different flavours. Use of colour and/or window is optional.

```html
<!DOCTYPE html>
<html lang="en">
<head>
<meta charset="utf-8">
<title>Copper Ridge Jerky – Pouch Range</title>
<link href="https://fonts.googleapis.com/css2?family=Oswald:wght@500;600&display=swap" rel="stylesheet">
<style>
  :root {
    --stage: #e4e4e4;
    --stage-light: #f2f2f2;
    --pouch-original: #3f2d52;
    --pouch-original-deep: #2f2140;
    --pouch-chilli: #2b2d5a;
    --pouch-chilli-deep: #202247;
    --moon-glow: rgba(150, 120, 175, 0.28);
    --silhouette: rgba(20, 14, 32, 0.75);
    --band: #1c1420;
    --band-edge: rgba(255, 255, 255, 0.18);
    --white: #f4f1ee;
    --gold: #e8b523;
    --yellow: #f2e21c;
    --red: #c2202a;
    --navy-ink: #262a72;
  }
  * { box-sizing: border-box; margin: 0; padding: 0; }
  html, body { width: 889px; height: 1200px; overflow: hidden; }
  body {
    background: linear-gradient(180deg, var(--stage) 0%, var(--stage-light) 50%, var(--stage) 100%);
    font-family: "Oswald", "Arial Narrow", sans-serif;
    position: relative;
  }
  .pouch {
    position: absolute;
    left: 176px;
    width: 540px;
    height: 504px;
    overflow: hidden;
    border-radius: 4px;
    box-shadow: 0 10px 24px rgba(0, 0, 0, 0.18);
  }
  .pouch--original { top: 68px; background: linear-gradient(180deg, var(--pouch-original) 0%, var(--pouch-original-deep) 100%); }
  .pouch--chilli { top: 644px; background: linear-gradient(180deg, var(--pouch-chilli) 0%, var(--pouch-chilli-deep) 100%); }

  .pouch__scene {
    position: absolute;
    left: 48px; top: 12px;
    width: 448px; height: 448px;
    border-radius: 50%;
    background: radial-gradient(circle at 50% 40%, var(--moon-glow) 0%, rgba(120, 100, 150, 0.14) 60%, transparent 72%);
  }
  .pouch__hills {
    position: absolute;
    left: 0; right: 0; top: 290px; height: 130px;
    background: linear-gradient(180deg, transparent 0%, rgba(15, 10, 25, 0.35) 100%);
  }
  .brand {
    position: absolute;
    left: 0; right: 0; top: 72px;
    text-align: center;
    color: var(--white);
  }
  .brand__tagline {
    font-size: 13px;
    font-weight: 500;
    letter-spacing: 4px;
    color: var(--gold);
    text-transform: uppercase;
  }
  .brand__name {
    margin-top: 40px;
    font-size: 54px;
    font-weight: 600;
    line-height: 1.05;
    letter-spacing: 2px;
    text-transform: uppercase;
    color: var(--white);
  }
  .pouch__animal {
    position: absolute;
    left: 212px; top: 284px;
    width: 136px; height: 116px;
    border-radius: 40% 45% 30% 30%;
    background: radial-gradient(ellipse at 50% 45%, var(--silhouette) 0%, rgba(20, 14, 32, 0.35) 70%, transparent 100%);
  }
  .label-band {
    position: absolute;
    left: 24px; right: 28px; top: 412px;
    height: 66px;
    background: var(--band);
    clip-path: polygon(4% 0, 96% 0, 100% 50%, 96% 100%, 4% 100%, 0 50%);
  }
  .label-band__frame {
    position: absolute;
    left: 18px; right: 18px; top: 6px; bottom: 6px;
    border-top: 1px solid var(--band-edge);
    border-bottom: 1px solid var(--band-edge);
  }
  .label-band__title {
    position: absolute;
    left: 0; right: 0; top: 2px;
    display: flex;
    justify-content: center;
    align-items: center;
    gap: 6px;
    font-size: 31px;
    font-weight: 500;
    color: var(--white);
    text-transform: uppercase;
    letter-spacing: -0.5px;
    line-height: 1.2;
  }
  .flavour-tag {
    background: var(--white);
    padding: 0 4px;
    line-height: 1.1;
    display: inline-flex;
    align-items: center;
    gap: 3px;
  }
  .flavour-tag--original { color: var(--red); }
  .flavour-tag--chilli { color: var(--navy-ink); }
  .flavour-tag__pepper {
    display: inline-block;
    width: 10px; height: 24px;
    border-radius: 6px;
    background: var(--red);
  }
  .label-band__weight {
    position: absolute;
    left: 0; right: 0; top: 40px;
    text-align: center;
    font-size: 20px;
    font-weight: 600;
    color: var(--yellow);
    line-height: 1;
  }
</style>
</head>
<body>

  <section class="pouch pouch--original" aria-label="Original flavour pouch">
    <div class="pouch__scene" role="img" aria-label="Moonlit mountain valley with pine forest"></div>
    <div class="pouch__hills" role="img" aria-label="Pine tree silhouettes"></div>
    <div class="brand">
      <p class="brand__tagline">Premium Cuts</p>
      <p class="brand__name">Copper Ridge<br>Jerky</p>
    </div>
    <div class="pouch__animal" role="img" aria-label="Bull silhouette"></div>
    <div class="label-band">
      <div class="label-band__frame"></div>
      <p class="label-band__title">
        <span>Copper Ridge</span>
        <span class="flavour-tag flavour-tag--original">Original</span>
        <span>Beef Jerky</span>
      </p>
      <p class="label-band__weight">60G</p>
    </div>
  </section>

  <section class="pouch pouch--chilli" aria-label="Chilli flavour pouch">
    <div class="pouch__scene" role="img" aria-label="Moonlit mountain valley with pine forest"></div>
    <div class="pouch__hills" role="img" aria-label="Pine tree silhouettes"></div>
    <div class="brand">
      <p class="brand__tagline">Premium Cuts</p>
      <p class="brand__name">Copper Ridge<br>Jerky</p>
    </div>
    <div class="pouch__animal" role="img" aria-label="Bull silhouette"></div>
    <div class="label-band">
      <div class="label-band__frame"></div>
      <p class="label-band__title">
        <span>Copper Ridge</span>
        <span class="flavour-tag flavour-tag--chilli"><span class="flavour-tag__pepper" role="img" aria-label="Red chilli pepper"></span>Chilli</span>
        <span>Beef Jerky</span>
      </p>
      <p class="label-band__weight">60G</p>
    </div>
  </section>

</body>
</html>
```